Website refresh

We are a leading provide of JTAG hardware and software tools. We provide affordable USB and Ethernet solutions that are easily integrated into applications via a common API for Windows and Linux platforms. Our product simplicity, integration with third party applications, and free utilities have made us the provider of choice for Paragon100 companies, small businesses as well as academic and research institutions.

JTAG is an industry standard interface by which hardware and software engineers can debug, test and program their hardware or software.

Target Market(s)

We are in the technology industry, and our target audience includes hardware engineers, low level embedded software engineers, and ASIC designers.

Industry/Entity Type

Software

Requirements
Must have
• The artwork for the slider must incorporate the product photos provided.

Our new website will be a facelift for our current website (www.quillmarsh-kits.net), and must allow all the content on the current website to be incorporate into the new website (the new website may have a new CMS).
Nice to have
• Please use the screen sketches as guidance. It does not have to follow this exactly, but should allow for the various elements to be incorporated.

The design I liked is by Tomas Berenholt - his Harbor template.
http://tomasberenholt.net/templates/harbor/

here is the live demo:
http://tomasberenholt.net/files/demo/harbor/

What do you think about this? Would welcome your opinion. My product is in black plastic:
http://www.quillmarsh-kits.net/index.php?main_page=corvane

so I hope that some picture of this (to replace the photos in the templates) will work well. (I will need to include landing
pages like the one above into the new site, and there will be a few like this for other potential customers)

I would be also nice to exchange some ideas on the scrolling/rolling logos for customers (company logos) an partners (company logos)

Please let me know your thoughts.

If you are also able to do web programming, or work with someone who might be able to assist with web programming and migrating the website (while incorporating the new template), then please let me know separately.

```html
<!DOCTYPE html>
<html lang="en">
<head>
<meta charset="utf-8">
<title>Quillmarsh – JTAG cables and tools</title>
<link rel="stylesheet" href="https://fonts.googleapis.com/css2?family=Asap:wght@400;500&family=Raleway:wght@500&display=swap">
<style>
  :root {
    --page-dark: #151515;
    --page-mid: #3a3a3a;
    --panel: #ffffff;
    --ink: #222222;
    --ink-soft: #333333;
    --brand: #8a5a9c;
    --accent: #c51ad2;
    --cart-red: #e0121c;
    --slide-deep: #081530;
    --slide-mid: #163060;
    --slide-copy: #a9b2c4;
    --rule: #dddddd;
    --tile: #e4e4e4;
    --tick: #5aa51e;
  }
  * { margin: 0; padding: 0; box-sizing: border-box; }
  html, body { width: 1200px; height: 785px; overflow: hidden; }
  body {
    position: relative;
    font-family: "Asap", sans-serif;
    color: var(--ink);
    background: radial-gradient(ellipse at 50% 0%, var(--page-mid) 0%, var(--page-dark) 70%);
  }
  .site { position: absolute; left: 140px; top: 37px; width: 921px; height: 708px; background: var(--panel); border-radius: 4px; }
  .brand { position: absolute; left: 20px; top: 30px; }
  .brand-name { font-size: 27px; font-weight: 500; color: var(--brand); line-height: 1; }
  .brand-tagline { font-size: 12.5px; color: var(--ink-soft); margin-top: 6px; white-space: nowrap; }
  .cart { position: absolute; left: 734px; top: 22px; display: flex; align-items: center; gap: 12px; color: var(--cart-red); font-size: 15.5px; white-space: nowrap; }
  .nav { position: absolute; top: 64px; left: 0; font-family: "Raleway", sans-serif; font-size: 14.5px; letter-spacing: .5px; }
  .nav a { position: absolute; top: 0; height: 29px; line-height: 29px; color: var(--ink-soft); text-decoration: none; white-space: nowrap; }
  .nav a.is-active { background: var(--brand); color: #fff; padding: 0 9px; }
  .slider { position: absolute; left: 20px; top: 112px; width: 882px; height: 312px;
    background: radial-gradient(ellipse at 22% 40%, var(--slide-mid) 0%, var(--slide-deep) 65%); }
  .slide-photo { position: absolute; left: 62px; top: 22px; width: 260px; height: 256px;
    background: radial-gradient(ellipse at 50% 55%, #8b93a2 0%, #4d5668 45%, rgba(8,21,48,0) 75%); }
  .slide-quote { position: absolute; left: 411px; top: 66px; width: 420px; color: #fff; font-size: 19px; line-height: 25px; text-align: center; }
  .slide-copy { position: absolute; left: 418px; top: 134px; width: 420px; color: var(--slide-copy); font-size: 13.2px; line-height: 21px; }
  .pager { position: absolute; left: 758px; top: 275px; display: flex; gap: 4px; }
  .pager span { width: 18px; height: 18px; background: #fff; color: #000; font-size: 12.5px; text-align: center; line-height: 18px; }
  .pager span.is-current { background: var(--accent); color: #fff; }
  .column { position: absolute; top: 434px; width: 244px; }
  .column h2 { font-weight: 400; font-size: 21px; color: var(--accent); padding-left: 2px; height: 38px; border-bottom: 1px solid var(--rule); white-space: nowrap; }
  .why { left: 28px; width: 256px; }
  .partners { left: 338px; }
  .products { left: 638px; }
  .checklist { list-style: none; margin-top: 8px; }
  .checklist li { display: flex; align-items: center; gap: 7px; font-size: 12.8px; height: 24.4px; line-height: 24.4px; color: var(--ink-soft); white-space: nowrap; }
  .checklist svg { flex: none; }
  .tile { position: absolute; top: 485px; width: 219px; height: 110px; background: var(--tile); border-radius: 6px; }
  .partner-tile { left: 347px; }
  .product-tile { left: 648px; }
  .partner-badge { position: absolute; left: 19px; top: 18px; width: 182px; height: 74px; background: #fff; border-radius: 6px; border: 1px solid #ccc; }
  .partner-badge i { position: absolute; left: 22px; top: 20px; width: 138px; height: 34px; background: #23457e; border-radius: 3px; }
  .product-shot { position: absolute; left: 22px; top: 22px; width: 175px; height: 69px; border: 3px solid #fff;
    background: linear-gradient(180deg, #a8a8dc 0%, #6f7d4e 55%, #a3a6d6 100%); }
  .divider { position: absolute; top: 437px; width: 8px; height: 204px;
    background: radial-gradient(ellipse at 0% 50%, rgba(0,0,0,.12) 0%, rgba(0,0,0,0) 70%); }
  .footer-shade { position: absolute; left: 20px; top: 650px; width: 880px; height: 10px;
    background: radial-gradient(ellipse at 50% 0%, rgba(0,0,0,.14) 0%, rgba(0,0,0,0) 70%); }
  .copyright { position: absolute; left: 22px; top: 676px; font-size: 12.5px; color: var(--ink); white-space: nowrap; }
  .legal { position: absolute; right: 19px; top: 677px; font-size: 12.5px; color: var(--ink); white-space: nowrap; }
  .legal a { color: inherit; text-decoration: none; }
</style>
</head>
<body>
  <div class="site">
    <header>
      <div class="brand">
        <div class="brand-name">Quillmarsh</div>
        <div class="brand-tagline">JTAG cables and tools for developers and engineers</div>
      </div>
      <div class="cart">
        <svg width="27" height="22" viewBox="0 0 27 22" aria-hidden="true">
          <path d="M1 3h5l4 11h12l3-8H8" fill="none" stroke="#777" stroke-width="2"/>
          <path d="M9 6h15l-2 7H11z" fill="#999"/>
          <circle cx="11" cy="18" r="2" fill="#666"/><circle cx="21" cy="18" r="2" fill="#666"/>
        </svg>
        <span>Shopping Cart (0)</span>
      </div>
      <nav class="nav">
        <a class="is-active" href="#" style="left:396px">PRODUCTS</a>
        <a href="#" style="left:552px">DOWNLOAD</a>
        <a href="#" style="left:708px">SUPPORT</a>
        <a href="#" style="left:844px">LOGIN</a>
      </nav>
    </header>

    <section class="slider">
      <div class="slide-photo" role="img" aria-label="Two JTAG adapter units, one white and one black, standing side by side"></div>
      <p class="slide-quote">"Neque porro quisquam est qui dolorem ipsum quia dolor sit amet, consectetur, adipisci velit..."</p>
      <p class="slide-copy">Lorem Ipsum is simply dummy text of the printing and typesetting industry. Lorem Ipsum has been the industry's standard dummy text ever since the 1500s, when an unknown printer took a galley of type and scrambled it to make a type specimen book.</p>
      <div class="pager"><span class="is-current">1</span><span>2</span><span>3</span><span>4</span><span>5</span></div>
    </section>

    <section class="column why">
      <h2>Why Us?</h2>
      <ul class="checklist">
        <li><svg width="13" height="11" viewBox="0 0 13 11" aria-hidden="true"><path d="M1 6l4 4 7-9" fill="none" stroke="var(--tick)" stroke-width="2.6"/></svg>Cras eu eros nibh, ut egestas dolor.</li>
        <li><svg width="13" height="11" viewBox="0 0 13 11" aria-hidden="true"><path d="M1 6l4 4 7-9" fill="none" stroke="var(--tick)" stroke-width="2.6"/></svg>Nunc eu odio metus, ut convallis ligula.</li>
        <li><svg width="13" height="11" viewBox="0 0 13 11" aria-hidden="true"><path d="M1 6l4 4 7-9" fill="none" stroke="var(--tick)" stroke-width="2.6"/></svg>Donec dignissim diam &nbsp;commodo lectus.</li>
        <li><svg width="13" height="11" viewBox="0 0 13 11" aria-hidden="true"><path d="M1 6l4 4 7-9" fill="none" stroke="var(--tick)" stroke-width="2.6"/></svg>Mauris dapibus massa in neque pretium.</li>
        <li><svg width="13" height="11" viewBox="0 0 13 11" aria-hidden="true"><path d="M1 6l4 4 7-9" fill="none" stroke="var(--tick)" stroke-width="2.6"/></svg>Duis at urna sapien, id elementum quam.</li>
      </ul>
    </section>

    <div class="divider" style="left:310px"></div>
    <section class="column partners"><h2>Patners</h2></section>
    <div class="tile partner-tile"><div class="partner-badge" role="img" aria-label="Partner badge"><i></i></div></div>

    <div class="divider" style="left:606px"></div>
    <section class="column products"><h2>Our Products</h2></section>
    <div class="tile product-tile"><div class="product-shot" role="img" aria-label="JTAG circuit boards"></div></div>

    <div class="footer-shade"></div>
    <footer>
      <p class="copyright">© 2012 Quillmarsh. All Rights Reserved.</p>
      <p class="legal"><a href="#">Terms &amp; conditions</a> | <a href="#">Policy</a> | <a href="#">Developers</a> | <a href="#">About Us</a> | <a href="#">Contact Us</a></p>
    </footer>
  </div>
</body>
</html>
```